依頼詳細
現在、既製品パッケージに入れて販売してますが、専用の袋を作りたいです。

盛り込むキーワード
◎商品名:はればれミックスナッツ
◎キャッチコピー:たべる時も、たべた後も、しあわせ。
◎無添加(無塩・無油)
◎葉月の膳ロゴ
◎リスが木の実を食べているイラスト

何種類かのパターンで販売するため、中身が見てわかるようにデザインしてほしいです。(面積で半分くらい透明部分になるように)
記載項目
袋サイズは、横210×縦310m
希望イメージ
シンプル 複雑
単色 カラフル
暗い 明るい
日常 高級
遊び心 厳粛
未来的 伝統的
女性的 男性的
希望する色
茶系、黄・オレンジ系
納品ファイル
• イラストレーター形式 (.ai)
• フォトショップ形式 (.psd)
もっと多くの作品を見たいので、5日間延長させていただきます。
■ 選んだ理由

森の動植物たちが、イメージにピッタリはまりました。

■ 提案者全員のお礼・コメント

今回初めてクラフタムを利用させていただきました。
短期間で非常に多くのご提案にビックリしましたし、また、その中から一つだけ選ぶのが大変でした。
今後も、引き続き商品パッケージの依頼をお願いすると思いますので、是非ご提案をよろしくお願いします。

```html
<!DOCTYPE html>
<html lang="ja">
<head>
<meta charset="utf-8">
<title>はればれミックスナッツ パッケージ</title>
<link rel="stylesheet" href="https://fonts.googleapis.com/css2?family=Klee+One:wght@600&family=Mochiy+Pop+One&family=Shippori+Mincho:wght@600&family=Zen+Maru+Gothic:wght@700&display=swap">
<style>
  :root {
    --paper: #f4eee3;
    --paper-edge: #e9e0cf;
    --crimp: #ddd2bd;
    --brown: #5a3a22;
    --brown-soft: #8a6240;
    --yellow: #f2c23a;
    --orange: #e9922f;
    --nut-light: #d9b98a;
    --nut-mid: #b07a45;
    --nut-dark: #7a4a28;
  }
  * { margin: 0; padding: 0; box-sizing: border-box; }
  html, body { width: 858px; height: 1200px; overflow: hidden; background: #ffffff; }
  .pouch {
    position: relative;
    width: 858px; height: 1200px;
    background: var(--paper);
    overflow: hidden;
  }
  .crimp {
    position: absolute; left: 0; width: 100%; height: 44px;
    background: repeating-linear-gradient(90deg, var(--paper-edge) 0 4px, var(--crimp) 4px 6px);
  }
  .crimp--top { top: 0; }
  .crimp--bottom { bottom: 0; }

  .badge {
    position: absolute; left: 118px; top: 120px;
    width: 150px; height: 130px;
    background: var(--yellow); border-radius: 18px;
    display: flex; flex-direction: column; align-items: center; justify-content: center;
    color: var(--brown);
    font-family: "Zen Maru Gothic", sans-serif;
  }
  .badge__main { font-size: 38px; letter-spacing: 2px; }
  .badge__sub { font-size: 20px; margin-top: 4px; }

  .catch {
    position: absolute; left: 320px; top: 95px;
    font-family: "Klee One", cursive;
    color: var(--brown);
    font-size: 36px; line-height: 1.45;
    transform: rotate(-4deg);
  }
  .catch__line2 { padding-left: 120px; }

  .squirrel {
    position: absolute; left: 580px; top: 185px;
    width: 140px; height: 130px;
    background: radial-gradient(circle at 45% 50%, #f0d9a8, #e2c08a);
    border-radius: 50% 45% 40% 50%;
  }

  .title {
    position: absolute; left: 0; top: 300px; width: 100%;
    text-align: center;
    font-family: "Mochiy Pop One", sans-serif;
    color: var(--brown);
  }
  .title__lead { display: block; font-size: 84px; line-height: 1.1; padding-left: 40px; }
  .title__main { display: block; font-size: 96px; line-height: 1.15; letter-spacing: 2px; }
  .title__burst { position: absolute; left: 175px; top: 300px; }

  .window { position: absolute; left: 0; top: 0; }

  .brand {
    position: absolute; left: 112px; top: 1010px;
    color: var(--brown);
    text-align: center;
  }
  .brand__name { font-family: "Shippori Mincho", serif; font-size: 50px; letter-spacing: 6px; }
  .brand__reading { font-family: "Zen Maru Gothic", sans-serif; font-size: 14px; letter-spacing: 4px; margin-top: 2px; }

  .mix-mark {
    position: absolute; left: 600px; top: 940px;
    width: 160px; height: 170px;
    background: linear-gradient(160deg, var(--orange), #d8792a);
    border-radius: 40% 50% 45% 35%;
    opacity: .85;
  }
</style>
</head>
<body>
<main class="pouch">
  <div class="crimp crimp--top"></div>
  <div class="crimp crimp--bottom"></div>

  <div class="badge">
    <span class="badge__main">無添加</span>
    <span class="badge__sub">無塩・無油</span>
  </div>

  <p class="catch">
    <span>たべる時も、たべた後も、</span><br>
    <span class="catch__line2">しあわせ。</span>
  </p>

  <div class="squirrel" role="img" aria-label="木の実を食べるリスのイラスト"></div>

  <svg class="title__burst" width="80" height="80" viewBox="0 0 80 80" aria-hidden="true">
    <g stroke="var(--yellow)" stroke-width="6" stroke-linecap="round">
      <line x1="60" y1="50" x2="20" y2="30"/>
      <line x1="60" y1="60" x2="15" y2="60"/>
      <line x1="62" y1="40" x2="40" y2="8"/>
    </g>
  </svg>

  <h1 class="title">
    <span class="title__lead">はればれ</span>
    <span class="title__main">ミックスナッツ</span>
  </h1>

  <svg class="window" width="858" height="1200" viewBox="0 0 858 1200" role="img" aria-label="透明窓から見えるミックスナッツ">
    <defs>
      <radialGradient id="nutFill" cx="50%" cy="55%" r="65%">
        <stop offset="0" stop-color="var(--nut-light)"/>
        <stop offset="0.55" stop-color="var(--nut-mid)"/>
        <stop offset="1" stop-color="var(--nut-dark)"/>
      </radialGradient>
    </defs>
    <path d="M150 560 C230 520 330 540 430 535 C540 530 640 520 720 555 C770 580 770 650 765 720 C760 820 770 920 750 1010 C735 1080 690 1120 600 1125 C480 1132 360 1128 250 1122 C170 1118 115 1090 105 1010 C95 900 100 780 105 680 C108 610 115 580 150 560 Z" fill="url(#nutFill)"/>
  </svg>

  <div class="brand">
    <p class="brand__name">葉月の膳</p>
    <p class="brand__reading">HAZUKI NO ZEN</p>
  </div>

  <div class="mix-mark" role="img" aria-label="手描き文字「Mix Nuts」"></div>
</main>
</body>
</html>
```